Business Card Design Project

i have the logo designed.
I require designs for the managing director and the general manager.
we need space for email, and a mobile number.
any other cool stuff/design you guys just let me see what you got.
The managing director card could be black, minimalist, and the cards for the rest of the company could be using the green logo.
it has to impress. transportation market is fragmented, we want to appear professional and sophisticated.
Md: Tarek bani rahim
General manager: omer rahim
clients: procurement heads of contracting companies
Business

```html
<!DOCTYPE html>
<html lang="en">
<head>
<meta charset="utf-8">
<title>Tarvane — Business Card Set</title>
<link href="https://fonts.googleapis.com/css2?family=Oxanium:wght@600&family=Orbitron:wght@600&family=Exo+2:ital,wght@1,500&display=swap" rel="stylesheet">
<style>
  :root {
    --ink: #1e1c1a;
    --paper: #ffffff;
    --edge: #d4d4d4;
    --canvas: #ffffff;
  }
  * { box-sizing: border-box; margin: 0; padding: 0; }
  html, body {
    width: 1200px; height: 746px; overflow: hidden;
    background: var(--canvas);
  }
  .sheet { position: relative; width: 1200px; height: 746px; }

  .card {
    position: absolute; width: 567px; height: 315px;
    background: var(--paper); overflow: hidden;
  }
  .card--logo-front { left: 0; top: 0; }
  .card--md-back { left: 633px; top: 0; border-bottom: 1px solid var(--edge); }
  .card--plain-front { left: 0; top: 428px; height: 316px; border: 1px solid var(--edge); }
  .card--side-back { left: 633px; top: 430px; height: 316px; border: 1px solid var(--edge); border-right: none; }

  .band { position: absolute; left: 0; width: 100%; background: var(--ink); }

  .brand {
    position: absolute; display: flex; align-items: center; gap: 10px;
    font-family: "Oxanium", sans-serif; font-weight: 600;
    font-size: 30px; letter-spacing: 1px; color: var(--ink);
  }
  .brand__dot { width: 14px; height: 14px; border-radius: 50%; background: var(--ink); }

  .person__name {
    font-family: "Orbitron", sans-serif; font-weight: 600;
    font-size: 20px; letter-spacing: 1px; line-height: 1;
  }
  .person__role {
    font-family: "Exo 2", sans-serif; font-style: italic; font-weight: 500;
    font-size: 14px; letter-spacing: .6px; line-height: 1;
  }
  .person__contact {
    font-family: "Exo 2", sans-serif; font-style: italic; font-weight: 500;
    font-size: 12px; line-height: 15px; letter-spacing: .8px;
  }

  .details--centered {
    position: absolute; left: 0; top: 171px; width: 100%;
    text-align: center; color: var(--paper);
  }
  .details--centered .person__role { margin-top: 23px; }
  .details--centered .person__contact { margin-top: 19px; }

  .details--right {
    position: absolute; right: 54px; top: 149px;
    text-align: right; color: var(--ink);
  }
  .details--right .person__role { margin-top: 23px; }
  .details--right .person__contact { margin-top: 11px; }
</style>
</head>
<body>
<main class="sheet">

  <section class="card card--logo-front" aria-label="Card front with brand">
    <div class="band" style="top:0;height:16px"></div>
    <div class="brand" style="left:208px;top:138px">
      <span class="brand__dot"></span><span>Tarvane</span>
    </div>
    <div class="band" style="top:298px;height:17px"></div>
  </section>

  <section class="card card--md-back" aria-label="Managing director card, banded">
    <div class="band" style="top:0;height:54px"></div>
    <div class="brand" style="left:213px;top:86px">
      <span class="brand__dot"></span><span>Tarvane</span>
    </div>
    <div class="band" style="top:157px;height:147px"></div>
    <div class="details--centered">
      <p class="person__name">Name Surname</p>
      <p class="person__role">Managing Director</p>
      <p class="person__contact">TEL.: 555 204 318<br>EMAIL.: office@tarvane.net</p>
    </div>
  </section>

  <section class="card card--plain-front" aria-label="Minimal card front">
    <div class="brand" style="left:350px;top:226px">
      <span class="brand__dot"></span><span>Tarvane</span>
    </div>
  </section>

  <section class="card card--side-back" aria-label="Managing director card, side bar">
    <div class="brand" style="left:30px;top:155px">
      <span class="brand__dot"></span><span>Tarvane</span>
    </div>
    <div class="details--right">
      <p class="person__name">Name Surname</p>
      <p class="person__role">Managing Director</p>
      <p class="person__contact">TEL.: 555 204 318<br>EMAIL.: office@tarvane.net</p>
    </div>
    <div class="band" style="top:0;left:547px;width:20px;height:100%"></div>
  </section>

</main>
</body>
</html>
```